【 概要 】 インスタ広告のバナーの制作依頼です。 サイズは1080x1080px 弊社のLPです。https://petgoods.shiranuiworkscollegeacad.net/ このLPを活かすバナーをお願いします。 【文言】 ペット好きのあなたがオリジナルブランドを作って ペット用品開発億万長者に アイデアを簡単に商品化!難しいことは○○にお任せ!自分の好きを仕事にできる! 無料オンライン説明会開催中 【注意事項】 ・画像の著作権は当方に譲渡されるものとします。 ・他媒体への流用を禁止します。 ・如何なる場合でも当方の画像や情報の漏洩は許されません。 ・納品後の画像の再利用は禁止です。 |
どの案も素敵でしたがこちらを採用させて頂きます。
皆様ご提案ありがとうございました。どれも個性的で良い提案ばかりでした。また機会があれば依頼させて頂きますので宜しくお願い致します。

```html
<!DOCTYPE html>
<html lang="ja">
<head>
<meta charset="utf-8">
<title>ペット用品開発 無料オンライン説明会</title>
<link rel="stylesheet" href="https://fonts.googleapis.com/css2?family=M+PLUS+Rounded+1c:wght@700;800&display=swap">
<style>
  :root{
    --bg:#b48f80;
    --panel:rgba(112,84,72,0.62);
    --panel-soft:rgba(130,98,86,0.55);
    --white:#ffffff;
    --orange:#f7a21c;
    --yellow:#fbbf2a;
    --ink:#4a3328;
    --photo-a:#e6dbd0;
    --photo-b:#c49a74;
  }
  *{margin:0;padding:0;box-sizing:border-box}
  html,body{width:1200px;height:1200px;overflow:hidden;background:var(--bg)}
  .banner{position:relative;width:1200px;height:1200px;background:var(--bg);
    font-family:"M PLUS Rounded 1c","Noto Sans JP",sans-serif;font-weight:800;overflow:hidden}
  .photo{position:absolute;left:53px;top:112px;width:710px;height:640px;
    background:radial-gradient(circle at 38% 42%,var(--photo-b) 0%,#d3b59c 50%,var(--photo-a) 100%)}
  .accent{position:absolute;border-radius:50%;background:var(--yellow)}
  .accent.top{left:905px;top:60px;width:200px;height:185px;opacity:.6}
  .accent.side{left:1085px;top:560px;width:170px;height:180px;opacity:.8}
  .panel{position:absolute;background:var(--panel)}
  .p-main{left:600px;top:55px;width:220px;height:710px}
  .p-brand{left:912px;top:25px;width:100px;height:790px}
  .p-lead{left:1055px;top:25px;width:80px;height:690px;background:var(--panel-soft)}
  .p-make{left:848px;top:545px;width:62px;height:255px;background:var(--panel-soft)}

  h1{font-weight:800}
  .col{position:absolute;display:flex;flex-direction:column;align-items:center}
  .col span{display:block;text-align:center;line-height:1}
  .lead{left:1063px;top:75px;color:var(--white);font-size:58px}
  .lead span{width:64px;height:63px}
  .brand{left:922px;top:60px;color:var(--orange);font-size:78px}
  .brand span{width:80px;height:82px}
  .make{left:852px;top:560px;color:var(--white);font-size:54px}
  .make span{width:54px;height:58px}
  .category{left:745px;top:80px;color:var(--white);font-size:56px}
  .category span{width:60px;height:64px}
  .million{left:620px;top:230px;color:var(--orange);font-size:108px}
  .million span{width:112px;height:112px}
  .to{left:648px;top:690px;color:var(--white);font-size:56px}
  .to span{width:56px;height:56px}

  .points{position:absolute;left:45px;top:848px;list-style:none}
  .point{display:flex;align-items:center;height:66px;margin-bottom:28px}
  .bullet{width:48px;height:48px;margin-right:24px}
  .pill{display:flex;align-items:center;height:66px;width:700px;padding-left:24px;
    border:4px solid var(--white);border-radius:14px;background:rgba(255,255,255,.12);
    font-size:42px;color:var(--white);letter-spacing:2px;white-space:nowrap}
  .pill em{font-style:normal;color:var(--orange)}
  .seminar{position:absolute;left:830px;top:800px;width:420px;height:380px}
  .seminar-text{position:absolute;left:845px;top:900px;width:400px;text-align:center;
    color:var(--ink);font-size:42px;line-height:1.3;letter-spacing:2px}
</style>
</head>
<body>
<div class="banner">
  <div class="photo" role="img" aria-label="こちらを見つめる薄茶色のトイプードルの写真"></div>
  <div class="accent top" role="img" aria-label="黄色の肉球の装飾"></div>
  <div class="accent side" role="img" aria-label="黄色の肉球の装飾"></div>

  <div class="panel p-main"></div>
  <div class="panel p-brand"></div>
  <div class="panel p-lead"></div>
  <div class="panel p-make"></div>

  <h1 aria-label="ペット好きのあなたがオリジナルブランドを作ってペット用品開発億万長者に">
    <span class="col lead" aria-hidden="true"><span>ペ</span><span>ッ</span><span>ト</span><span>好</span><span>き</span><span>の</span><span>あ</span><span>な</span><span>た</span><span>が</span></span>
    <span class="col brand" aria-hidden="true"><span>オ</span><span>リ</span><span>ジ</span><span>ナ</span><span>ル</span><span>ブ</span><span>ラ</span><span>ン</span><span>ド</span></span>
    <span class="col make" aria-hidden="true"><span>を</span><span>作</span><span>っ</span><span>て</span></span>
    <span class="col category" aria-hidden="true"><span>ペ</span><span>ッ</span><span>ト</span><span>用</span><span>品</span><span>開</span><span>発</span></span>
    <span class="col million" aria-hidden="true"><span>億</span><span>万</span><span>長</span><span>者</span></span>
    <span class="col to" aria-hidden="true"><span>に</span></span>
  </h1>

  <ul class="points">
    <li class="point">
      <svg class="bullet" viewBox="0 0 48 48"><circle cx="24" cy="24" r="16" fill="#4a3328"/></svg>
      <span class="pill">アイデアを簡単に<em>商品化</em>！</span>
    </li>
    <li class="point">
      <svg class="bullet" viewBox="0 0 48 48"><circle cx="24" cy="24" r="16" fill="#4a3328"/></svg>
      <span class="pill">難しいことは○○に<em>お任せ</em>！</span>
    </li>
    <li class="point">
      <svg class="bullet" viewBox="0 0 48 48"><circle cx="24" cy="24" r="16" fill="#4a3328"/></svg>
      <span class="pill">自分の<em>好き</em>を仕事にできる！</span>
    </li>
  </ul>

  <svg class="seminar" viewBox="0 0 420 380" aria-hidden="true">
    <defs>
      <radialGradient id="seminarFill" cx="50%" cy="45%" r="60%">
        <stop offset="0%" stop-color="#fdd25a"/>
        <stop offset="100%" stop-color="#fbb82a"/>
      </radialGradient>
    </defs>
    <ellipse cx="215" cy="195" rx="205" ry="172" fill="url(#seminarFill)"/>
  </svg>
  <p class="seminar-text">無料<br>オンライン<br>説明会開催中</p>
</div>
</body>
</html>
```